its a new company based in Christchurch new Zealand building computers ,repairs, upgrades and anything computers for the general public,i like bright happy colours like yellows, greens reds anything that stands out and it needs to communicant trust and security towards my new company,i have no logo yet,

Target Market(s)

target market of all ages

Industry/Entity Type

Building

Contact Information for Business Card

Pixel Harbour Limited,ph-0274829315,email-brightnode47@mailvista.example,14c tamworth cl,kelvale

```html
<!DOCTYPE html>
<html lang="en">
<head>
<meta charset="utf-8">
<title>Pixel Harbour Limited – Business Card</title>
<link rel="stylesheet" href="https://fonts.googleapis.com/css2?family=Questrial&family=Open+Sans:wght@700&display=swap">
<style>
  :root {
    --lime: #9fff2c;
    --ink: #070707;
    --tile: #c3cbc8;
    --tile-edge: #ffffff;
  }
  * { margin: 0; padding: 0; box-sizing: border-box; }
  html, body {
    width: 1200px;
    height: 741px;
    overflow: hidden;
    background: var(--lime);
  }
  .card {
    position: relative;
    width: 1200px;
    height: 741px;
    background: var(--lime);
    overflow: hidden;
  }
  .card__bands {
    position: absolute;
    inset: 0;
    width: 1200px;
    height: 741px;
  }
  .brand {
    position: absolute;
    left: 158px;
    top: 150px;
    display: flex;
    align-items: center;
    gap: 26px;
  }
  .brand__square {
    width: 82px;
    height: 84px;
    background: var(--tile);
    border: 2px solid var(--tile-edge);
    flex: none;
  }
  .brand__name {
    font-family: "Questrial", sans-serif;
    font-weight: 400;
    font-size: 76px;
    line-height: 80px;
    color: var(--ink);
    letter-spacing: -0.5px;
  }
  .contact {
    position: absolute;
    left: 548px;
    top: 385px;
    font-family: "Open Sans", sans-serif;
    font-weight: 700;
    font-size: 31px;
    line-height: 43px;
    color: var(--ink);
    list-style: none;
  }
</style>
</head>
<body>
  <main class="card">
    <svg class="card__bands" viewBox="0 0 1200 741" aria-hidden="true">
      <polygon class="top-tab" points="368,0 838,0 780,84 424,84" fill="var(--ink)"/>
      <polygon class="bottom-band" points="0,592 378,592 432,640 795,640 845,592 1200,592 1200,741 0,741" fill="var(--ink)"/>
    </svg>

    <div class="brand">
      <span class="brand__square"></span>
      <h1 class="brand__name">Pixel Harbour<br>Limited</h1>
    </div>

    <ul class="contact">
      <li class="contact__phone">PH-0274829315</li>
      <li class="contact__email">email-brightnode47@mailvista.example</li>
      <li class="contact__street">14C Tamworth CL</li>
      <li class="contact__suburb">Kelvale</li>
    </ul>
  </main>
</body>
</html>
```